Mirabel Dunstow writer

I need a design for my business cards I write verses quotes and put them on to canvas, for children adults.
I like the idea of a quill pen and I love colour and a bit of magic as words can be magical.
My email address is verneloft@mailquill.example PH: 0400817342
Here is an example of what I write
Can you put this verse on it
WORDS
Words can bring a tear to the eye
Words can make a heart sigh
Words can colour a world thats bland
Words can help one understand

This one is just a sample of my type of writing to give you an idea of the feel i'm looking for.
You'r Freind
I promise to be there
When life seems unfair
Sit with you when you cry
Wiping that tear from your eye
Holding you through the pain
Until you smile again
On me you can depend
Always your friend
Mirabel Dunstow (c)

Target Market(s)

My target market is everyone family friend lover .

Industry/Entity Type

Business

Colors

Designer to choose colors to be used in the design.

```html
<!DOCTYPE html>
<html lang="en">
<head>
<meta charset="utf-8">
<title>Mirabel Dunstow – Business Card</title>
<link href="https://fonts.googleapis.com/css2?family=Parisienne&family=Varela+Round&display=swap" rel="stylesheet">
<style>
  :root {
    --stage: #808080;
    --ink: #1f1a18;
    --gold: #c8a76a;
    --gold-light: #d6b77c;
    --gold-mid: #b8995e;
    --gold-deep: #7d5f33;
    --cream: #ffffff;
    --edge: #3a3028;
  }
  * { margin: 0; padding: 0; box-sizing: border-box; }
  html, body { width: 931px; height: 1200px; overflow: hidden; background: var(--stage); }
  .canvas { position: relative; width: 931px; height: 1200px; }

  .card {
    position: absolute;
    left: 86px;
    width: 758px;
    height: 490px;
    border-radius: 26px;
    border: 1px solid var(--edge);
    overflow: hidden;
  }
  .card-front { top: 124px; background: var(--ink); }
  .card-back {
    top: 634px;
    background: linear-gradient(90deg, #a58550 0%, var(--gold-mid) 25%, #c09f64 50%, #a3854f 75%, var(--gold-deep) 100%);
  }

  .verse-title {
    position: absolute;
    left: 0; width: 758px; top: 20px;
    text-align: center;
    font-family: "Parisienne", cursive;
    font-size: 66px;
    color: var(--gold);
    line-height: 1;
  }
  .verse {
    position: absolute;
    left: 56px; top: 110px;
    list-style: none;
    font-family: "Parisienne", cursive;
    font-size: 37px;
    line-height: 59px;
    color: var(--gold);
  }
  .signature {
    position: absolute;
    right: 178px; top: 352px;
    font-family: "Parisienne", cursive;
    font-size: 31px;
    color: var(--gold);
  }
  .quill {
    position: absolute;
    left: 586px; top: 174px;
    width: 240px; height: 212px;
  }

  .contact-band {
    position: absolute;
    left: 0; bottom: 0;
    width: 100%; height: 82px;
    background: linear-gradient(90deg, var(--gold-mid), var(--gold-light) 55%, var(--gold-mid));
    display: flex; align-items: center; justify-content: center;
    font-family: "Varela Round", sans-serif;
    font-size: 24px;
    letter-spacing: 1px;
    color: var(--cream);
  }
  .contact-band .divider {
    width: 2px; height: 40px; background: var(--cream);
    margin: 0 16px;
  }

  .back-name {
    position: absolute;
    left: 0; width: 100%; top: 220px;
    text-align: center;
    font-family: "Varela Round", sans-serif;
    font-size: 46px;
    color: var(--ink);
    letter-spacing: 1px;
  }
</style>
</head>
<body>
<main class="canvas">
  <section class="card card-front">
    <h1 class="verse-title">Words</h1>
    <ul class="verse">
      <li>Words can bring a tear to the eye</li>
      <li>Words can make a heart sigh</li>
      <li>Words can colour a world thats bland</li>
      <li>Words can help one understand</li>
    </ul>
    <p class="signature">Mirabel Dunstow (c)</p>
    <svg class="quill" role="img" aria-label="Golden quill pen illustration with ink flourish" viewBox="0 0 240 212">
      <defs>
        <linearGradient id="quillTone" x1="0" y1="1" x2="1" y2="0">
          <stop offset="0" stop-color="#a8782e"/>
          <stop offset="1" stop-color="#e0a93c"/>
        </linearGradient>
      </defs>
      <polygon points="0,212 240,212 240,0" fill="url(#quillTone)" opacity="0.35"/>
    </svg>
    <div class="contact-band">
      <span class="email">verneloft@mailquill.example</span>
      <span class="divider"></span>
      <span class="phone">PH: 0400817342</span>
    </div>
  </section>

  <section class="card card-back">
    <p class="back-name">Mirabel Dunstow (c)</p>
  </section>
</main>
</body>
</html>
```